Market online tutoring + Back to School + give Support for students school work K to 12 Grade

To promote my tutoring business online need to create a two sided flyer. Need to get the attention of parents and educators who looking for help to support the digital learning of their students due to COVID-19 lock down. I need to project and differentiate that we offer support for online school with individualized learning . We tutor Elementary to High school students on all subjects you may take a look at my website qnacademyga.com for additional info and also I can provide
Updates

Hi All Due to Covid, we were unable to work on this project on time as originally planned. We were given an extension until March 15 and we will complete it by then. Sorry for any inconvenience and Thank you for your support. -QN Academy

Target Market(s)

Parents and students

Industry/Entity Type

Education

Requirements
Must have
• For online less fine print on the first page. The phone number and support text message. Back to School , Support Online learning KEV/NUR test prep should have some focus
Nice to have
• Discuss the platform We created a platform with live instructor interaction, virtual classroom, instructional videos, assessments, and practice to support every individual student’s need. We are confident in our ability to provide the most effective distance learning experience.
Should not have
• too much clunky and packed with content. Should be easy to read with color

```html
<!DOCTYPE html>
<html lang="en">
<head>
<meta charset="utf-8">
<title>QN Academy – Two-Sided Flyer</title>
<link rel="stylesheet" href="https://fonts.googleapis.com/css2?family=Crimson+Text:wght@600;700&family=Roboto:wght@400;500&display=swap">
<style>
  :root {
    --navy: #25536d;
    --navy-deep: #1c4259;
    --red: #c8202f;
    --red-soft: #d94a55;
    --ink: #3a3a3a;
    --paper: #ffffff;
    --backdrop: #dfe3e0;
    --serif: "Crimson Text", Georgia, serif;
    --sans: "Roboto", Arial, sans-serif;
  }
  * { box-sizing: border-box; margin: 0; padding: 0; }
  html, body { width: 1200px; height: 2400px; overflow: hidden; background: var(--backdrop); }
  .flyer-page {
    position: absolute; left: 160px; width: 880px; height: 1140px;
    background: var(--paper); overflow: hidden;
    box-shadow: -14px 14px 0 rgba(0,0,0,0.14);
  }
  .flyer-front { top: 40px; }
  .flyer-back { top: 1220px; }
  .page-shapes { position: absolute; inset: 0; width: 880px; height: 1140px; }

  .brand { position: absolute; left: 50px; top: 62px; display: flex; align-items: center; gap: 16px; }
  .brand-mark { width: 34px; height: 34px; background: var(--red); }
  .brand-name { font-family: var(--serif); font-weight: 600; font-size: 40px; color: var(--navy); letter-spacing: 1px; }

  .headline { position: absolute; left: 40px; top: 172px; font-family: var(--serif); font-weight: 700; color: var(--navy); line-height: 1; }
  .headline-lead { font-size: 36px; letter-spacing: 0.5px; }
  .headline-main { display: block; font-size: 82px; color: var(--red); letter-spacing: 1px; line-height: 0.98; margin-top: 8px; }
  .headline-sub { display: block; font-size: 23px; margin-top: 8px; letter-spacing: 0.3px; }

  .photo { position: absolute; }
  .photo-laptop { left: 0; top: 520px; width: 400px; height: 300px; }

  .intro { position: absolute; left: 424px; top: 540px; width: 400px; }
  .section-title { font-family: var(--serif); font-weight: 700; color: var(--navy); font-size: 22px; line-height: 1.15; text-transform: uppercase; margin-bottom: 12px; }
  .body-copy { font-family: var(--sans); font-size: 12.5px; line-height: 1.38; color: var(--ink); text-align: justify; }
  .body-copy + .body-copy { margin-top: 14px; }

  .contact { position: absolute; left: 58px; font-family: var(--sans); color: #fff; }
  .flyer-front .contact { top: 976px; }
  .flyer-back .contact { top: 980px; }
  .contact-title { font-family: var(--serif); font-weight: 700; font-size: 20px; color: var(--red-soft); margin-bottom: 14px; }
  .contact-line { display: flex; align-items: flex-start; gap: 8px; font-size: 14px; line-height: 1.3; margin-bottom: 12px; }
  .contact-line svg { flex: none; margin-top: 2px; }

  .course-col { position: absolute; top: 52px; width: 355px; }
  .course-col.left { left: 52px; }
  .course-col.right { left: 470px; width: 360px; }
  .course { margin-bottom: 18px; }
  .course-title { font-family: var(--serif); font-weight: 700; font-size: 16px; color: var(--red); text-transform: uppercase; line-height: 1.1; }
  .course-note { font-family: var(--serif); font-weight: 700; font-size: 11px; color: var(--ink); text-transform: uppercase; margin-bottom: 6px; }
  .course-title + .course-text { margin-top: 6px; }
  .course-text { font-family: var(--sans); font-size: 11.5px; line-height: 1.34; color: var(--ink); text-align: justify; }
  .course-text + .course-text { margin-top: 10px; }
  .course-list { list-style: none; font-family: var(--sans); font-size: 11.5px; color: var(--ink); margin-top: 6px; }
  .course-list.inline { display: flex; gap: 20px; }
  .course-list li::before { content: "\2022"; color: var(--red); margin-right: 5px; }
</style>
</head>
<body>

<!-- FRONT SIDE -->
<section class="flyer-page flyer-front">
  <svg class="page-shapes" viewBox="0 0 880 1140" aria-hidden="true">
    <path d="M0 468 Q300 520 560 400 Q700 335 880 250 L880 280 Q700 372 560 432 Q300 540 0 500 Z" fill="var(--navy)"/>
    <path d="M0 452 Q300 500 560 386 Q700 320 880 232 L880 252 Q700 338 560 402 Q300 522 0 470 Z" fill="var(--red)"/>
    <path d="M0 890 Q260 845 600 852 L880 870 L880 1140 L0 1140 Z" fill="var(--red)"/>
    <path d="M0 922 Q260 876 600 880 L880 896 L880 1140 L0 1140 Z" fill="var(--navy)"/>
    <path d="M520 868 Q680 852 880 880 L880 888 Q680 864 520 874 Z" fill="var(--navy-deep)"/>
    <path d="M440 35 Q660 -15 880 25 L880 330 Q790 450 665 475 Q520 395 468 250 Z" fill="var(--red)"/>
    <path d="M460 50 Q660 8 880 42 L880 318 Q785 430 665 455 Q535 380 485 245 Z" fill="var(--navy)"/>
  </svg>

  <div class="brand">
    <span class="brand-mark"></span>
    <span class="brand-name">QN ACADEMY</span>
  </div>

  <h1 class="headline">
    <span class="headline-lead">WE SUPPORT THE</span>
    <span class="headline-main">DIGITAL<br>LEARNING</span>
    <span class="headline-sub">DUE TO COVID-19 LOCKDOWN</span>
  </h1>

  <svg class="photo" style="left:0;top:0" width="880" height="480" role="img" aria-label="Photo of two high school students studying together at a library table">
    <defs><linearGradient id="studentsTone" x1="0" y1="0" x2="1" y2="1"><stop offset="0" stop-color="#8a6f58"/><stop offset="1" stop-color="#c9c2b6"/></linearGradient></defs>
    <path d="M474 62 Q660 22 880 54 L880 312 Q782 420 665 443 Q545 372 498 244 Z" fill="url(#studentsTone)"/>
  </svg>

  <div class="photo photo-laptop" role="img" aria-label="Illustration of an open book turning into a laptop with floating learning icons" style="background:radial-gradient(ellipse at 60% 55%, #dfe6ec 0%, #f4f6f8 55%, #ffffff 80%);"></div>

  <div class="intro">
    <h2 class="section-title">A Place to Enrich<br>Students' Potentials</h2>
    <p class="body-copy">QN Academy in Larkfield, Georgia is a private tutoring center which provides group coaching in Math, Reading, KEV Preparation, and Computer Programming for kids. We are proud to offer a curriculum that is truly unique, providing a strong focus on advanced coaching in Math and Reading.</p>
    <p class="body-copy">We also provide effective coaching for standardized tests like KEV, ITRA, etc. We step away from the regular coaching method and implement effective problem solving techniques and critical thinking skills to help our children achieve stronger academic results.</p>
  </div>

  <div class="photo" role="img" aria-label="Photo of a smiling tutor helping a young boy with his schoolwork" style="left:455px;top:810px;width:425px;height:330px;background:linear-gradient(160deg,#e9e3d6 0%,#b9ab8f 45%,#6c7272 100%);border-top-left-radius:180px 120px;"></div>

  <div class="contact">
    <p class="contact-title">CONTACT US</p>
    <p class="contact-line">
      <svg width="12" height="15" viewBox="0 0 12 15"><path d="M6 0a6 6 0 0 0-6 6c0 4.5 6 9 6 9s6-4.5 6-9a6 6 0 0 0-6-6z" fill="var(--red-soft)"/><circle cx="6" cy="6" r="2.2" fill="var(--navy)"/></svg>
      <span>4520 Harlow Creek Rd, Suite 210<br>Larkfield, GA 30099</span>
    </p>
    <p class="contact-line">
      <svg width="14" height="11" viewBox="0 0 14 11"><rect width="14" height="11" rx="1" fill="var(--red-soft)"/><path d="M1 1l6 5 6-5" stroke="var(--navy)" stroke-width="1.3" fill="none"/></svg>
      <span>customerservice@qnacademyga.com</span>
    </p>
    <p class="contact-line">
      <svg width="13" height="13" viewBox="0 0 13 13"><path d="M3 0l2 3-1.4 1.6a8 8 0 0 0 4.8 4.8L10 8l3 2-1.3 2.6C6 13 0 7 .4 1.3z" fill="var(--red-soft)"/></svg>
      <span>555-014-2273</span>
    </p>
  </div>
</section>

<!-- BACK SIDE -->
<section class="flyer-page flyer-back">
  <svg class="page-shapes" viewBox="0 0 880 1140" aria-hidden="true">
    <path d="M0 898 Q300 845 620 835 L880 840 L880 1140 L0 1140 Z" fill="var(--red)"/>
    <path d="M0 930 Q300 875 620 866 L880 870 L880 1140 L0 1140 Z" fill="var(--navy)"/>
    <path d="M0 882 Q300 830 620 822 L880 826 L880 832 Q620 830 300 838 Q120 856 0 890 Z" fill="var(--navy-deep)"/>
    <path d="M460 785 Q660 705 880 735 L880 1140 L610 1140 Q470 1000 460 785 Z" fill="var(--red)"/>
    <path d="M478 796 Q660 725 880 752 L880 1140 L630 1140 Q490 1005 478 796 Z" fill="var(--navy)"/>
  </svg>

  <div class="course-col left">
    <div class="course">
      <h3 class="course-title">Mathematics</h3>
      <p class="course-note">(Georgia Standard of Education)</p>
      <p class="course-text">Help young learners build the conceptual understanding needed to tackle more complex mathematical challenges. Provide rigorous instruction on Georgia Standards of Excellence. Develop mathematical reasoning through lessons that use real-world problem solving as instruction. We teach young learners to solve problems that also require the application of higher-order thinking skills. Adopt appropriate type and method of teaching for students at various skill levels.</p>
    </div>
    <div class="course">
      <h3 class="course-title">KEV Preparation</h3>
      <p class="course-text">Our dedicated teachers are specialized and highly experienced in KEV preparation, nurture students to achieve higher scores to enter into their top choice colleges. "Practice Makes Perfect" We get the kids in to a routine of consistent practice of various concepts required for success in KEV test.</p>
    </div>
    <div class="course">
      <h3 class="course-title">Critical Thinking</h3>
      <p class="course-text">Our critical thinking courses are specially designed to make kids to use in-depth analysis of evidence to make decisions and communicate their beliefs clearly and accurately. Kids with good critical thinking skills produces better grades and higher test scores. Our fun and easy to learn courses makes students to analyze deeper which produces deeper understanding of subject.</p>
    </div>
    <div class="course">
      <h3 class="course-title">Computer Science</h3>
      <p class="course-text">QN Academy offers computer science training with strong focus on Programming. We provide age appropriate computer science training which includes valuable concepts of computer programming with comprehensive training for a variety of software applications and key areas like:</p>
      <p class="course-text">DeskSuite office - HTML Web design - Serpa Programming - Kava Programming - Computer Architecture - Nimbus Programming - Orbit Programming - Fun Programming for young kids</p>
    </div>
    <div class="course">
      <h3 class="course-title">Robotics</h3>
      <p class="course-text">Robot building offers students a platform for learning areas about science, technology, engineering and math (STEM). Students learn how science and engineering principles work together to solve real world problems. We offer following robot building classes for all age groups,</p>
      <ul class="course-list inline"><li>BrickBot Mind Kit</li><li>VORTA Robotics</li></ul>
    </div>
  </div>

  <div class="course-col right">
    <div class="course">
      <h3 class="course-title">Reading</h3>
      <p class="course-note">(GSE)</p>
      <p class="course-text">Build strong reading comprehension skills with the right balance of informational and literacy text from a wide range of genres. Promote comprehension skills in emergent readers and provide rigorous instruction on every reading standard in a developmentally appropriate way.</p>
      <p class="course-text">Provide instructions required to meet higher expectations and teach students to become independent, critical thinkers. Focused on improving Language Fluency Phonetic Awareness, Reading Compression, and Vocabulary skills.</p>
    </div>
    <div class="course">
      <h3 class="course-title">Writing</h3>
      <p class="course-note">(GSE)</p>
      <p class="course-text">Our writing program helps student organize and articulate their own ideas to become confident, competent writers and thinkers. In this program, students will learn all types of writing; Argumentative, Informative, Scientific, and Narrative writing. Participants in this program will also learn about writing structure, correct grammar, review writing strategies, and much more.</p>
      <p class="course-text">We help students learn the techniques to make their work powerful and exciting. The materials used in this program will be aligned to their GSE standards. We help students experience a feeling of confidence and pride when they turn in their work.</p>
    </div>
    <div class="course">
      <h3 class="course-title">Custom Courses</h3>
      <p class="course-text">QN Academy will be able to provide the service you need to "Excel your Goals and Achieve". Do you have different need other than our standard offerings? Please contact us we will customize our offerings to meet your need.</p>
      <ul class="course-list">
        <li>One-one-one tutoring</li>
        <li>Accelerated programs</li>
        <li>Tutoring for Science, Social Studies and Others</li>
      </ul>
    </div>
  </div>

  <svg class="photo" style="left:0;top:0" width="880" height="1140" role="img" aria-label="Photo of a teacher presenting at a whiteboard to a classroom of students">
    <defs><linearGradient id="classroomTone" x1="0" y1="0" x2="0" y2="1"><stop offset="0" stop-color="#e8e8e4"/><stop offset="0.6" stop-color="#b7a998"/><stop offset="1" stop-color="#5b5048"/></linearGradient></defs>
    <path d="M492 806 Q660 742 880 768 L880 1140 L648 1140 Q505 1010 492 806 Z" fill="url(#classroomTone)"/>
  </svg>

  <div class="contact">
    <p class="contact-title">CONTACT US</p>
    <p class="contact-line">
      <svg width="12" height="15" viewBox="0 0 12 15"><path d="M6 0a6 6 0 0 0-6 6c0 4.5 6 9 6 9s6-4.5 6-9a6 6 0 0 0-6-6z" fill="var(--red-soft)"/><circle cx="6" cy="6" r="2.2" fill="var(--navy)"/></svg>
      <span>4520 Harlow Creek Rd, Suite 210<br>Larkfield, GA 30099</span>
    </p>
    <p class="contact-line">
      <svg width="14" height="11" viewBox="0 0 14 11"><rect width="14" height="11" rx="1" fill="var(--red-soft)"/><path d="M1 1l6 5 6-5" stroke="var(--navy)" stroke-width="1.3" fill="none"/></svg>
      <span>customerservice@qnacademyga.com</span>
    </p>
    <p class="contact-line">
      <svg width="13" height="13" viewBox="0 0 13 13"><path d="M3 0l2 3-1.4 1.6a8 8 0 0 0 4.8 4.8L10 8l3 2-1.3 2.6C6 13 0 7 .4 1.3z" fill="var(--red-soft)"/></svg>
      <span>555-014-2273</span>
    </p>
  </div>
</section>

</body>
</html>
```